Supplement Label Design - Sports Nutrition

Design a sports nutrition/weight loss supplement label that stands out in a crowded space. Supplement bottle size is 200c and label size is 7" x 2.5" approximately. We're looking for a design that emphasizes the products name called VUK. Vuk is an abbreviation for Vigor, Uplift & Keenness. We want VUK to be the center/focus point of the bottle and have a memorable design to it.

Target Market(s)

Men & Women over 18

Industry/Entity Type

Supplement

Font styles to use
Sans Serif
Decorative

Requirements
Must have
• Emphasis on the product name VUK. Serious, Inspirational & Motivational feel to the design, typo & colors. Electrocution/lightning feel to the text. Right hand side of label is our formulation. Left hand side is dedicated to explaining the trifecta formulation idea.
Nice to have
• For example, we like the graphic design of "Thud" energy drinks because you can identify the bottle from a distance and is memorable. We think that less is more and we'd like the design/colors do most of the talking.
Should not have
• Cartroon/animated style.

```html
<!DOCTYPE html>
<html lang="en">
<head>
<meta charset="utf-8">
<title>VUK Weight Loss Supplement Label</title>
<link href="https://fonts.googleapis.com/css2?family=Saira+Condensed:wght@400;500;600;700&family=Open+Sans:ital,wght@0,400;0,600;0,700;1,400&family=Archivo+Black&display=swap" rel="stylesheet">
<style>
  :root {
    --page: #ffffff;
    --label: #1c1a1b;
    --label-deep: #0f0e0f;
    --red: #c0353c;
    --red-dark: #7a1a20;
    --white: #f4f2f2;
    --rule: #8a8788;
  }
  * { box-sizing: border-box; margin: 0; padding: 0; }
  html, body { width: 1200px; height: 900px; overflow: hidden; background: var(--page); }
  .canvas { position: relative; width: 1200px; height: 900px; }
  .label {
    position: absolute; left: 20px; top: 140px; width: 1160px; height: 620px;
    background: radial-gradient(ellipse at 50% 40%, var(--label) 0%, var(--label-deep) 100%);
    color: var(--white); overflow: hidden;
  }
  .label-streaks { position: absolute; inset: 0; }
  .panel { position: absolute; top: 0; height: 100%; }

  /* left: formulation story */
  .panel-story { left: 0; width: 400px; padding: 70px 26px 0 34px; font-family: "Saira Condensed", sans-serif; }
  .story-title { font-size: 27px; font-weight: 500; line-height: 1.2; margin-bottom: 12px; }
  .story-body { font-size: 16px; line-height: 1.45; text-align: justify; }
  .story-callout { margin-top: 24px; border: 2px solid var(--white); padding: 10px 14px; font-size: 16px; line-height: 1.45; }
  .story-foot { display: flex; gap: 24px; margin-top: 22px; align-items: center; }
  .story-blank { width: 170px; height: 86px; background: var(--white); flex: none; }
  .story-note { font-size: 16px; line-height: 1.45; }

  /* center: brand */
  .panel-brand { left: 400px; width: 360px; text-align: center; font-family: "Saira Condensed", sans-serif; line-height: 1; }
  .brand-kicker { position: absolute; top: 56px; width: 100%; font-size: 30px; font-weight: 600; letter-spacing: 4px; }
  .brand-maker { position: absolute; top: 128px; width: 100%; font-size: 62px; font-weight: 700; letter-spacing: 3px; }
  .brand-name { position: absolute; top: 196px; width: 100%; font-size: 220px; font-weight: 700; color: var(--red); letter-spacing: 4px; }
  .brand-claim { position: absolute; top: 458px; width: 100%; font-size: 46px; font-weight: 700; letter-spacing: 2px; }
  .brand-type { position: absolute; top: 560px; width: 100%; font-size: 30px; font-weight: 600; letter-spacing: 1px; }

  /* right: formulation */
  .panel-facts { left: 760px; width: 400px; padding: 40px 20px 0 34px; font-family: "Open Sans", sans-serif; }
  .facts-table { border: 1px solid var(--rule); padding: 4px 6px 2px; }
  .facts-title { font-family: "Archivo Black", sans-serif; font-size: 29px; line-height: 1.2; }
  .facts-row { display: flex; font-size: 10.5px; line-height: 17px; border-top: 1px solid var(--rule); }
  .facts-row.is-plain { border-top: none; }
  .facts-row .name { flex: 1; }
  .facts-row .amt { width: 30px; text-align: right; }
  .facts-row .unit { width: 30px; text-align: center; }
  .facts-row .dv { width: 32px; text-align: right; font-size: 9px; }
  .facts-row.is-blend { font-weight: 700; }
  .facts-row.is-sub .name { padding-left: 8px; }
  .facts-extra { font-size: 10.5px; line-height: 17px; margin-top: 8px; }
  .facts-extra b { font-weight: 600; }
  .seal-row { display: flex; justify-content: space-between; margin-top: 16px; padding-right: 4px; }
  .seal { width: 66px; height: 66px; border-radius: 50%; background: var(--white); }
</style>
</head>
<body>
<div class="canvas">
  <div class="label">
    <svg class="label-streaks" width="1160" height="620" viewBox="0 0 1160 620" aria-hidden="true">
      <g fill="none" stroke="var(--red-dark)" stroke-width="3" opacity="0.85">
        <path d="M300 0 L0 380"/>
        <path d="M0 560 L140 450"/>
        <path d="M400 190 L0 205"/>
        <path d="M880 0 L1160 330"/>
        <path d="M1010 0 L1160 180"/>
        <path d="M760 200 L1160 230"/>
        <path d="M770 470 L1100 620"/>
      </g>
      <g fill="none" stroke="var(--red)" stroke-width="2.5">
        <path d="M408 175 L445 112 L715 112 L752 175"/>
        <path d="M404 560 L470 440 L690 440 L756 560"/>
        <path d="M420 620 L460 548 L700 548 L740 620"/>
      </g>
    </svg>

    <section class="panel panel-story">
      <h2 class="story-title">Lorem ipsum</h2>
      <p class="story-body">Lorem ipsum dolor sit amet, consectetuer adipiscing elit, sed diam nonummy nibh euismod tincidunt ut laoreet dolore magna aliquam erat volutpat. Ut wisi enim ad minim veniam, quis nostrud exerci tation. Lorem ipsum dolor sit amet, consectetuer adipiscing elit, sed diam nonummy nibh euismod tincidunt ut laoreet dolore magna aliquam erat volutpat. Ut wisi enim ad minim veniam, quis nostrud exerci tation</p>
      <p class="story-callout">Lorem ipsum dolor sit amet, consectetuer adipiscing elit, sed diam nonummy nibh euismod tincidunt ut laoreet dolore magna aliquam erat volutpat.</p>
      <div class="story-foot">
        <div class="story-blank"></div>
        <p class="story-note">Lorem ipsum dolor amet, consectetuer adipiscing elit, dolore magna aliquam erat.</p>
      </div>
    </section>

    <section class="panel panel-brand">
      <p class="brand-kicker">UPLIFT &amp; KEENNESS</p>
      <p class="brand-maker">KINETRIX</p>
      <h1 class="brand-name">VUK</h1>
      <p class="brand-claim">WEIGHT LOSS</p>
      <p class="brand-type">SUPPLEMENT</p>
    </section>

    <section class="panel panel-facts">
      <div class="facts-table">
        <h2 class="facts-title">Supplement Facts</h2>
        <div class="facts-row is-plain"><span class="name">Serving Size: 2 capsules</span><span>Servings Per Container: 30</span></div>
        <div class="facts-row"><span class="name">Amount per Serving</span><span class="dv">%DV</span></div>
        <div class="facts-row"><span class="name">Niacin (as niacinamide)</span><span class="amt">40</span><span class="unit">mg</span><span class="dv">250%</span></div>
        <div class="facts-row"><span class="name">Vitamin B6 (as pyridoxal-5-phosphate)</span><span class="amt">8.5</span><span class="unit">mg</span><span class="dv">500%</span></div>
        <div class="facts-row"><span class="name">Vitamin B12 (as methylcobalamin)</span><span class="amt">12</span><span class="unit">mcg</span><span class="dv">500%</span></div>
        <div class="facts-row is-blend"><span class="name">Proprietary Vigor Blend</span><span class="amt">450</span><span class="unit">mg</span><span class="dv">*</span></div>
        <div class="facts-row is-sub"><span class="name">Ashwagandha Root Extract (<i>Withania somnifera</i>)</span><span class="dv">*</span></div>
        <div class="facts-row is-sub"><span class="name">Acetyl L-Carnitine HCl</span><span class="dv">*</span></div>
        <div class="facts-row is-sub"><span class="name">L-Theanine</span><span class="dv">*</span></div>
        <div class="facts-row is-blend"><span class="name">Proprietary Uplift Blend</span><span class="amt">425</span><span class="unit">mg</span><span class="dv">*</span></div>
        <div class="facts-row is-sub"><span class="name"><i>Garcinia cambogia</i> extract (fruit)</span><span class="dv">*</span></div>
        <div class="facts-row is-sub"><span class="name">Yohimbe Bark Extract (<i>Pausinystalia johimbe</i>)</span><span class="dv">*</span></div>
        <div class="facts-row is-sub"><span class="name">Capsiforce® (capsicum fruit extract)<br>(standardized to 2% capsaicinoids)</span><span class="amt"><br>320</span><span class="unit"><br>mg</span><span class="dv">*</span></div>
        <div class="facts-row is-blend"><span class="name">Proprietary Keenness Blend (215 mg Caffeine)</span><span class="dv">*</span></div>
        <div class="facts-row is-sub"><span class="name">Green Tea Extract</span><span class="dv">*</span></div>
        <div class="facts-row is-sub"><span class="name">Theobromine</span><span class="dv">*</span></div>
        <div class="facts-row is-sub"><span class="name">Green Coffee Fruit Extract</span><span class="dv">*</span></div>
        <div class="facts-row"><span class="name">*Daily Value (DV) not established</span></div>
      </div>
      <p class="facts-extra"><b>Other Ingredients:</b> Rice flour, L-leucine, hypromellose (capsule).<br><b>Warning:</b> Contains 215 mg of caffeine per serving.</p>
      <div class="seal-row">
        <span class="seal"></span><span class="seal"></span><span class="seal"></span><span class="seal"></span>
      </div>
    </section>
  </div>
</div>
</body>
</html>
```